Capability Statement Brochure - Corporate

We need to provide our corporate clients with an elegant, professional and well designed capability statement that not only details what our business can offer, but reflects our professionalism with relevant technical photos. I am thinking two pages A 4 pdf will be suitable if the text can fit without looking crowded but happy to extend to 3 or 4 pages if needed . Colours and details can be taken from our website www.quorintech.com.au Some photos have been attached however if we need more professional stock photos I am happy to use them if needed. This project needs to convince potential clients we are the best in industry and our capability is extensive. Please help us relay this to our customers. Thank you,.

Target Market(s)

Corporate, Government, Education, Defence, Healthcare

Industry/Entity Type

Audio Visual Integration

Colors
0054AA
0677BA
7BADD7
CADEEF
E8F1F8

Requirements
Must have
• Style, look classy, sophisticated and technical
Nice to have
• Quorin Tech colours, Logo, website and email and include the PRISM LED Logo
Should not have
• Messy, too much clutter, not easy to read.

```html
<!DOCTYPE html>
<html lang="en">
<head>
<meta charset="utf-8">
<title>Quorin Tech Systems – Capability Statement</title>
<link rel="stylesheet" href="https://fonts.googleapis.com/css2?family=Montserrat:wght@400;500;600;700;800&display=swap">
<style>
  :root{
    --blue-deep:#2a55b0;
    --blue-brand:#0054aa;
    --blue-mid:#0677ba;
    --blue-light:#6fb0e2;
    --blue-pale:#cadeef;
    --blue-mist:#e8f1f8;
    --accent:#e8862a;
    --ink:#1d1d24;
    --text:#4a4d57;
    --page:#ffffff;
    --bg:#dfe3e8;
    --grey-bar:#ececee;
  }
  *{box-sizing:border-box;margin:0;padding:0}
  html,body{width:1200px;height:900px;overflow:hidden}
  body{background:var(--bg);font-family:"Montserrat",sans-serif;color:var(--text);position:relative}
  .page{position:absolute;top:56px;width:540px;height:764px;background:var(--page);box-shadow:0 6px 22px rgba(0,0,0,.14);overflow:hidden}
  .page--front{left:40px}
  .page--back{left:620px}

  /* front header */
  .masthead{height:74px;display:flex;align-items:center;justify-content:space-between;padding:0 28px}
  .brand{display:flex;align-items:center;gap:10px}
  .brand__mark{width:18px;height:18px;background:var(--ink);flex:none}
  .brand__name{font-size:14px;font-weight:700;color:var(--ink);letter-spacing:.2px}
  .brand__tag{display:block;font-size:6px;font-weight:500;letter-spacing:.6px;color:var(--text);text-transform:uppercase;margin-top:3px}
  .product-name{font-size:14px;font-weight:800;color:var(--ink);letter-spacing:.5px;text-align:right}
  .product-name small{display:block;font-size:7px;color:var(--ink);letter-spacing:1.5px;font-weight:800}

  .hero{position:relative;height:222px;display:flex}
  .hero__photo{width:48%;height:100%;background:linear-gradient(135deg,#e9ecef 0%,#c9cdd2 55%,#8a7f72 100%)}
  .hero__panel{position:relative;flex:1;background:var(--blue-deep);color:#fff;padding:52px 26px 0 46px;overflow:hidden}
  .hero__band{position:absolute;left:-30px;top:0;width:46px;height:100%;background:var(--blue-light);transform:skewX(-14deg)}
  .hero__band--two{left:8px;width:14px;background:#9ac8ec}
  .hero__eyebrow{position:relative;font-size:12px;font-weight:400;padding-bottom:6px;border-bottom:1px solid var(--accent);display:inline-block}
  .hero__title{position:relative;font-size:32px;font-weight:800;line-height:1;margin-top:8px}
  .hero__subtitle{position:relative;font-size:20px;font-weight:700;margin-top:4px}
  .hero__corner{position:absolute;right:0;bottom:0;width:40px;height:40px}

  .front-body{padding:18px 28px 0}
  .section-title{font-size:15px;font-weight:700;color:var(--ink);margin-bottom:8px}
  .section-title::after{content:"";display:block;width:60px;height:1px;background:var(--accent);margin-top:5px}
  .copy{font-size:6.8px;line-height:1.55;margin-bottom:6px}
  .columns{display:flex;gap:26px;margin-top:12px}
  .columns>div{flex:1}
  .ticks{list-style:none;font-size:6.8px;line-height:1.75}
  .ticks li{position:relative;padding-left:10px}
  .ticks li::before{content:"";position:absolute;left:0;top:4px;width:4px;height:4px;border-radius:50%;background:var(--accent)}

  .markets{padding:14px 28px 0}
  .markets__grid{display:flex;gap:8px}
  .market{width:72px;height:62px;background:var(--blue-deep);color:#fff;display:flex;flex-direction:column;align-items:center;justify-content:center;gap:5px;font-size:5.8px;font-weight:600;text-align:center;line-height:1.2}
  .market svg{width:16px;height:16px}

  /* back page */
  .back-photo{position:absolute;left:0;top:0;width:100%;height:172px;background:linear-gradient(120deg,#d8d2c3 0%,#efefec 45%,#3a3b3f 80%,#f2f2f0 100%)}
  .sectors{position:absolute;left:0;top:130px;width:300px;height:600px;background:var(--blue-deep);color:#fff;padding:22px 18px 0 0}
  .bar{position:relative;display:flex;align-items:center;gap:6px;height:20px;background:var(--blue-light);color:#fff;font-size:9px;font-weight:700;padding-left:14px;margin-bottom:6px;clip-path:polygon(0 0,100% 0,94% 100%,0 100%)}
  .bar__icon{width:11px;height:11px;border-radius:50%;background:#fff;flex:none}
  .sector{margin-bottom:10px}
  .sector .copy{padding-left:14px;color:#fff;font-size:6.4px;margin-bottom:3px}
  .services{position:absolute;left:320px;top:186px;width:200px}
  .services .bar{font-size:8.4px;margin-bottom:7px}
  .services .copy{font-size:6.4px;padding-left:4px}
  .service{margin-bottom:12px}
  .why{position:absolute;left:320px;top:548px;width:200px}
  .why__title{font-size:13px;font-weight:700;color:var(--ink);line-height:1.15;margin-bottom:10px}
  .why__list{list-style:none}
  .why__list li{position:relative;background:var(--grey-bar);font-size:6.4px;padding:4px 6px 4px 16px;margin-bottom:4px}
  .why__list li::before{content:"";position:absolute;left:6px;top:6px;width:4px;height:4px;border-radius:50%;background:var(--accent)}
  .web{position:absolute;left:330px;top:736px;font-size:8px;font-weight:700;color:var(--ink);display:flex;align-items:center;gap:5px}
  .web__dot{width:8px;height:8px;border-radius:50%;background:var(--blue-mid)}
</style>
</head>
<body>

<section class="page page--front">
  <header class="masthead">
    <div class="brand">
      <span class="brand__mark"></span>
      <div><span class="brand__name">Quorin Tech Systems</span><span class="brand__tag">Audiovisual integration specialists</span></div>
    </div>
    <div class="product-name">PRISM<small>LED VIDEO WALL</small></div>
  </header>

  <div class="hero">
    <div class="hero__photo" role="img" aria-label="Photo of a bright corporate boardroom with meeting table, chairs and wall display"></div>
    <div class="hero__panel">
      <span class="hero__band"></span><span class="hero__band hero__band--two"></span>
      <p class="hero__eyebrow">Quorin Tech Systems</p>
      <h1 class="hero__title">Capability</h1>
      <p class="hero__subtitle">Statement</p>
      <svg class="hero__corner" viewBox="0 0 40 40"><polygon points="10,40 40,10 40,40" fill="#6fb0e2"/><polygon points="0,30 10,20 10,40" fill="#ffffff"/></svg>
    </div>
  </div>

  <div class="front-body">
    <h2 class="section-title">Company Overview</h2>
    <p class="copy">Quorin Tech Systems (QTS) is a leading Australian audiovisual integration specialist delivering advanced AV, unified communications, collaboration environments, and large-scale digital display systems across Australia.</p>
    <p class="copy">With more than 25 years of industry experience, QTS provides end-to-end services including system design, engineering, installation, commissioning, and long-term technical support. Our solutions enable organisations to communicate, collaborate, and share information effectively across boardrooms, control centres, training environments, operational facilities, and large public spaces.</p>
    <p class="copy">QTS works across a broad range of sectors including healthcare, corporate enterprise, government, defence, mining and resources, and education. Our team combines deep technical expertise with a strong understanding of operational environments where reliability, security, and ease of use are essential.</p>

    <div class="columns">
      <div>
        <h2 class="section-title">Company Overview</h2>
        <ul class="ticks">
          <li>AV System Design and Engineering</li>
          <li>Unified Communications and Collaboration Systems</li>
          <li>LED Video Walls and Large Format Displays</li>
          <li>Control Rooms and Operations Centres</li>
          <li>Boardrooms and Executive Meeting Spaces</li>
          <li>Education and Training Environments</li>
          <li>Digital Signage and Information Display Networks</li>
          <li>AV over IP and Networked Media Systems</li>
          <li>System Programming, Automation and Control</li>
          <li>Ongoing Service, Maintenance and Technical Support</li>
        </ul>
      </div>
      <div>
        <h2 class="section-title">LED Video Wall Expertise</h2>
        <p class="copy">Quorin Tech Systems has extensive experience designing and installing direct-view LED video walls for corporate environments, education facilities, public venues, and large presentation spaces.</p>
        <p class="copy">Our proprietary PRISM LED video wall solutions provide exceptional brightness, durability, and reliability for high-impact display environments such as school halls, gymnasiums, corporate auditoriums, and public venues.</p>
        <p class="copy">QTS provides complete LED video wall solutions including structural design, engineering certification, installation, commissioning, and ongoing support.</p>
      </div>
    </div>
  </div>

  <div class="markets">
    <h2 class="section-title">Markets Served</h2>
    <div class="markets__grid">
      <div class="market"><svg viewBox="0 0 16 16"><path d="M8 14 2 8a3.4 3.4 0 0 1 6-4 3.4 3.4 0 0 1 6 4z" fill="#fff"/></svg>Healthcare</div>
      <div class="market"><svg viewBox="0 0 16 16"><rect x="4" y="2" width="8" height="13" fill="#fff"/></svg>Corporate &amp; Enterprise</div>
      <div class="market"><svg viewBox="0 0 16 16"><polygon points="8,1 15,5 1,5" fill="#fff"/><rect x="2" y="6" width="2" height="6" fill="#fff"/><rect x="7" y="6" width="2" height="6" fill="#fff"/><rect x="12" y="6" width="2" height="6" fill="#fff"/><rect x="1" y="13" width="14" height="2" fill="#fff"/></svg>Government</div>
      <div class="market"><svg viewBox="0 0 16 16"><path d="M8 1 14 3v5c0 4-3 6-6 7-3-1-6-3-6-7V3z" fill="#fff"/></svg>Defence</div>
      <div class="market"><svg viewBox="0 0 16 16"><polygon points="1,5 15,5 12,12 4,12" fill="#fff"/><circle cx="5" cy="14" r="1.4" fill="#fff"/><circle cx="11" cy="14" r="1.4" fill="#fff"/></svg>Mining &amp; Resources</div>
      <div class="market"><svg viewBox="0 0 16 16"><rect x="6" y="2" width="9" height="7" fill="#fff"/><circle cx="3" cy="6" r="2" fill="#fff"/><rect x="1" y="9" width="4" height="6" fill="#fff"/></svg>Education</div>
      <div class="market"><svg viewBox="0 0 16 16"><rect x="2" y="4" width="12" height="11" fill="#fff"/><rect x="5" y="1" width="6" height="3" fill="#fff"/></svg>Public Venues &amp; Event Spaces</div>
    </div>
  </div>
</section>

<section class="page page--back">
  <div class="back-photo" role="img" aria-label="Photo of a computer training room with rows of desks and monitors"></div>

  <div class="sectors">
    <div class="sector"><div class="bar"><span class="bar__icon"></span>Healthcare Experience</div>
      <p class="copy">QTS has extensive experience delivering audiovisual solutions within major healthcare environments including clinical communication systems, specialist consultation rooms, training facilities, and hospital-wide digital signage networks.</p>
      <p class="copy">For over 20 years QTS has supported Westbrook General Hospital with the design, implementation and support of audiovisual infrastructure across departments including ICU, Emergency, Cardiology, Radiology, and Allied Health.</p></div>
    <div class="sector"><div class="bar"><span class="bar__icon"></span>Corporate &amp; Enterprise</div>
      <p class="copy">QTS delivers modern collaboration environments that enable organisations to connect teams across offices, remote staff, and global partners.</p>
      <p class="copy">Solutions include boardrooms, hybrid meeting rooms, training facilities, corporate digital signage networks, and executive collaboration spaces.</p></div>
    <div class="sector"><div class="bar"><span class="bar__icon"></span>Government &amp; Defence</div>
      <p class="copy">QTS supports government departments and defence organisations with reliable and secure audiovisual systems designed for operational environments including command centres, training facilities, situation rooms, and secure conferencing spaces.</p></div>
    <div class="sector"><div class="bar"><span class="bar__icon"></span>Mining &amp; Resources</div>
      <p class="copy">QTS provides robust AV systems designed for industrial and remote environments including operations centres, training rooms, induction facilities, and remote collaboration systems supporting mining and energy sector operations.</p></div>
    <div class="sector"><div class="bar"><span class="bar__icon"></span>Education</div>
      <p class="copy">QTS delivers innovative AV solutions for schools, universities, and training institutions including lecture theatres, classrooms, hybrid learning environments, school halls, gymnasiums, and large-scale LED display systems.</p></div>
    <div class="sector"><div class="bar"><span class="bar__icon"></span>Design &amp; Engineering</div>
      <p class="copy">QTS provides comprehensive in-house design and engineering services including system architecture, documentation, schematics, networked AV design, and integration with existing IT infrastructure.</p>
      <p class="copy">Our team works closely with architects, consultants, builders, and project managers to ensure seamless integration of audiovisual technology within new builds and refurbishment projects.</p></div>
  </div>

  <div class="services">
    <div class="service"><div class="bar"><span class="bar__icon"></span>Implementation &amp; Commissioning</div>
      <p class="copy">QTS delivers complete turnkey project implementation including equipment procurement, professional installation, system configuration, testing, commissioning, and user training.</p>
      <p class="copy">Our accredited technicians ensure systems are delivered safely, efficiently, and with minimal disruption to operational environments.</p></div>
    <div class="service"><div class="bar"><span class="bar__icon"></span>Service &amp; Support</div>
      <p class="copy">QTS provides comprehensive ongoing support services including preventative maintenance, priority service response, remote diagnostics, system upgrades, and technology lifecycle planning.</p>
      <p class="copy">Our long-term support partnerships ensure systems remain reliable, secure, and aligned with evolving organisational needs.</p></div>
    <div class="service"><div class="bar"><span class="bar__icon"></span>Governance, Safety &amp; Compliance</div>
      <p class="copy">QTS operates under strict safety and governance frameworks including OH&amp;S compliant work practices, industry-certified technicians, and full public liability and professional indemnity coverage.</p>
      <p class="copy">Safety, compliance, and quality assurance are embedded throughout all project delivery activities.</p></div>
  </div>

  <div class="why">
    <h2 class="why__title">Why Choose<br>Quorin Tech Systems</h2>
    <ul class="why__list">
      <li>25+ years audiovisual integration experience</li>
      <li>Proven track record across multiple industries</li>
      <li>In-house design and engineering capability</li>
      <li>National project delivery capability</li>
      <li>LED video wall specialists</li>
      <li>Long-term service and support partnerships</li>
    </ul>
  </div>
  <p class="web"><span class="web__dot"></span>www.quorintech.com.au</p>
</section>

</body>
</html>
```